Banner for Vet Hospital 5m x 1.2m - Heat Stroke

Maplecourt Pet Hospital needs a Heat Stroke Banner for Summer.
The banner will be 5000mm long and 1200mm tall.

Our region has been hot this year and this summer is going to be extremely hot.
I want to warn people about heat stroke.
I want you to create a heat stroke banner that conveys the symptoms of heat stroke.

Pictures are better than words.
There should be IMAGES and WORDS that can be seen from the road 30m away and maybe some smaller words for people to read as they walk past.

Here are some of the signs of Heat Stroke:
- Panting which increases as heatstroke progresses
- Drooling, salivating
- Agitation, restlessness
- Very red or pale gums
- Bright red tongue
- Increased heart rate
- Breathing distress
- Vomiting Diarrhea (possibly with blood)
- Signs of mental confusion, delirium
- Dizziness, staggering
- Lethargy, weakness
- Muscle tremors
- Seizures
- Collapsing and lying down
- Little to no urine production
- Coma

I have attached characters that we often use in our advertising. They are optional.
I have done a mock up of the design I imagine. You could refine this design or make your own....or both.

Target Market(s)

Women aged 20 to 50.

Industry/Entity Type

Veterinary

Font styles to use
Sans Serif

Colors
fbed22
f78f20
ec1f27
ffffff

Requirements
Must have
• Heat Stroke Symtpms.
• Heat Stroke Warning.
• Summer theme.
Nice to have
• Bright colours.

```html
<!DOCTYPE html>
<html lang="en">
<head>
<meta charset="utf-8">
<title>Heat Stroke Can Kill – Maplecourt Pet Hospital</title>
<link rel="stylesheet" href="https://fonts.googleapis.com/css2?family=Arimo:wght@700&display=swap">
<style>
  :root {
    --sun-yellow: #fbed22;
    --ray-gold: #fbd21e;
    --ray-amber: #f9b51f;
    --ray-orange: #f78f20;
    --alert-red: #ec1f27;
    --ink: #1a1a1a;
    --white: #ffffff;
    --coat-tan: #b9774a;
    --coat-cream: #f3e6d4;
  }
  * { margin: 0; padding: 0; box-sizing: border-box; }
  html, body { width: 1200px; height: 288px; overflow: hidden; background: var(--sun-yellow); }
  .banner {
    position: relative;
    width: 1200px;
    height: 288px;
    overflow: hidden;
    font-family: "Arimo", Arial, sans-serif;
    font-weight: 700;
  }
  .sunburst { position: absolute; inset: 0; }
  .sun-title {
    position: absolute;
    left: 579px;
    top: 10px;
    transform: translateX(-50%);
    color: var(--alert-red);
    font-size: 21px;
    line-height: 25px;
    text-align: center;
    white-space: nowrap;
  }
  .symptom {
    position: absolute;
    color: var(--ink);
    font-size: 19px;
    line-height: 1;
    white-space: nowrap;
  }
  .dog {
    position: absolute;
    border-radius: 40% 40% 30% 30%;
    background: radial-gradient(ellipse at 50% 40%, var(--coat-cream) 0%, var(--coat-tan) 70%);
    opacity: 0.9;
  }
  .dog--panting { left: 140px; top: 84px; width: 110px; height: 196px; }
  .dog--distressed { left: 334px; top: 110px; width: 168px; height: 172px; }
  .dog--lying { left: 622px; top: 162px; width: 186px; height: 120px; border-radius: 50% 50% 20% 20%; }
  .dog--collapsed { left: 920px; top: 112px; width: 276px; height: 128px; border-radius: 45%; }
  .site-address {
    position: absolute;
    right: 16px;
    bottom: 8px;
    color: var(--ink);
    font-size: 15px;
  }
</style>
</head>
<body>
<main class="banner">
  <svg class="sunburst" width="1200" height="288" viewBox="0 0 1200 288" aria-hidden="true">
    <rect width="1200" height="288" fill="var(--sun-yellow)"/>
    <polygon points="579,23 0,0 0,60" fill="var(--ray-gold)"/>
    <polygon points="579,23 0,150 0,230" fill="var(--ray-gold)"/>
    <polygon points="579,23 150,288 300,288" fill="var(--ray-amber)"/>
    <polygon points="579,23 500,288 600,288" fill="var(--ray-gold)"/>
    <polygon points="579,23 760,288 900,288" fill="var(--ray-amber)"/>
    <polygon points="579,23 1200,200 1200,288 1100,288" fill="var(--ray-gold)"/>
    <polygon points="579,23 1200,40 1200,140" fill="var(--ray-orange)"/>
    <polygon points="579,23 750,0 1200,0 1200,30" fill="var(--ray-orange)"/>
    <polygon points="579,23 200,0 330,0" fill="var(--ray-amber)"/>
    <circle cx="579" cy="18" r="98" fill="var(--ray-orange)"/>
    <circle cx="579" cy="18" r="90" fill="var(--sun-yellow)"/>
  </svg>

  <h1 class="sun-title">HEAT STROKE<br>CAN KILL</h1>

  <div class="dog dog--panting" role="img" aria-label="Cartoon dog sitting and panting with tongue out"></div>
  <div class="dog dog--distressed" role="img" aria-label="Cartoon dog hunched over, dizzy and unwell"></div>
  <div class="dog dog--lying" role="img" aria-label="Cartoon dog lying flat, confused and weak"></div>
  <div class="dog dog--collapsed" role="img" aria-label="Cartoon dog collapsed on its back"></div>

  <p class="symptom" style="left:37px; top:58px;">Excessive Panting</p>
  <p class="symptom" style="left:25px; top:122px;">Drooling</p>
  <p class="symptom" style="left:34px; top:180px;">Agitation</p>
  <p class="symptom" style="left:296px; top:82px;">Breathing Distress</p>
  <p class="symptom" style="left:266px; top:183px;">Diarrhea</p>
  <p class="symptom" style="left:582px; top:122px;">Confusion</p>
  <p class="symptom" style="left:562px; top:168px;">Vomiting</p>
  <p class="symptom" style="left:791px; top:62px;">Muscle Tremors</p>
  <p class="symptom" style="left:797px; top:110px;">Collapse</p>
  <p class="symptom" style="left:831px; top:160px;">Coma</p>

  <p class="site-address">maplecourtpethospital.com.au</p>
</main>
</body>
</html>
```